Presentation for partners template design for a healthy bakery

A bakery that makes healthy homemade cupcakes, needs a presentation template for wholesale partners. We need 3-4 template pages with pictures and text blocks, one template that can accomodate a pricing table. Just to give you an idea for the templates our final presentation will include:
1. Cover page with logo
2. Intro page about us
3. Detailed description of products
4. Menu table: cupcakes with wholesale pricing
5. Contact page
Updates

Target Market(s)

Food stores, cafés, fitness clubs, pastry shops, etc.

Industry/Entity Type

Bakery

Font styles to use
Sans Serif

Colors
fee3d4
fce8d3
eaf2ce
cadf82
ffffff
000000
cfeae6
ec1f27
86cfc6

Requirements
Must have
• Presentation needs to look serious and professional. The design needs to give an eco feel: we use recycled materials in our packaging and production. Please make sure the fonts you use support Cyrillic.
Nice to have
• The format of pages is either square or horizontal A4. The company mint colour (see logo attached) needs to be used, but other colours can be used in addition (lime green, peach, black, chocolate brown, red, etc). Craft paper texture (like our packaging, see photos) would be nice to have.

```html
<!DOCTYPE html>
<html lang="en">
<head>
<meta charset="utf-8">
<title>Bramblecakes – Partner Presentation Template</title>
<link href="https://fonts.googleapis.com/css2?family=Montserrat:wght@300;400;600;700&family=Open+Sans:wght@400;600&family=Dancing+Script:wght@500&display=swap" rel="stylesheet">
<style>
:root{
  --mint:#86cfc6;
  --mint-light:#cfeae6;
  --page:#dde5e2;
  --page-edge:#cdd8d4;
  --ink:#4e5b59;
  --ink-soft:#7d8a88;
  --white:#ffffff;
  --backdrop:#f3f5f4;
  --choc:#6b4a3d;
  --peach:#fee3d4;
  --rose:#d99fb4;
}
*{box-sizing:border-box;margin:0;padding:0}
html,body{width:1200px;height:1200px;overflow:hidden}
body{background:var(--backdrop);font-family:"Open Sans",Arial,sans-serif;color:var(--ink)}
.board{width:1200px;height:1200px;padding:26px 20px;display:grid;grid-template-columns:570px 570px;grid-auto-rows:360px;gap:22px 20px;justify-content:center}
.spread{display:flex;background:var(--page);box-shadow:0 4px 14px rgba(60,80,76,.18);position:relative}
.spread::after{content:"";position:absolute;left:50%;top:0;bottom:0;width:10px;margin-left:-5px;background:linear-gradient(90deg,transparent,rgba(0,0,0,.08),transparent)}
.spread--center{grid-column:1 / span 2;width:570px;justify-self:center}
.page{width:285px;height:360px;position:relative;padding:22px 18px 30px;overflow:hidden;border-top:4px solid var(--mint)}
.page--bleed{padding:0;border-top:none}
.photo{display:block;background:radial-gradient(circle at 35% 35%,var(--rose),var(--choc) 75%)}
.photo--round{border-radius:50%;border:4px solid var(--white);box-shadow:0 0 0 2px var(--mint)}
.photo--choc{background:radial-gradient(circle at 40% 40%,#8a5a3c,#3e2a22 70%,#d9c07a)}
.photo--carrot{background:radial-gradient(circle at 50% 45%,#e69a55,#f4dcb8 55%,#b7c9a2)}
.photo--berry{background:radial-gradient(circle at 40% 50%,#e7a6c3,#7b6aa8 65%,#5a5a6a)}
.photo--warm{background:linear-gradient(135deg,#b58a84,#d9b7a8 50%,#a7c8a7)}
.photo--mint{background:linear-gradient(135deg,#6b4a3d,#86cfc6 45%,#a8ddd6 70%,#6b4a3d)}
.photo--kitchen{background:linear-gradient(160deg,#c9b09c,#f0e2d4 50%,#8d6c5c)}
.h-title{font-family:"Montserrat",Arial,sans-serif;font-weight:600;color:var(--ink);font-size:12px;line-height:1.2}
.h-title span{font-weight:300}
.h-big{font-family:"Montserrat",Arial,sans-serif;font-weight:700;font-size:20px;letter-spacing:.5px}
.h-big span{font-weight:300}
.body-text{font-size:6.2px;line-height:1.55;color:var(--ink-soft);margin-top:6px}
.body-text b{color:var(--ink);font-weight:600}
.script{font-family:"Dancing Script",cursive;color:var(--mint);font-size:11px;line-height:1.25;margin-top:6px}
.footer{position:absolute;left:18px;right:18px;bottom:12px;display:flex;align-items:center;gap:6px;font-family:"Montserrat",Arial,sans-serif;font-size:5.5px;font-weight:600;letter-spacing:.6px;color:var(--ink)}
.footer::after{content:"";flex:1;height:1px;background:var(--mint)}
.mark{position:absolute;right:14px;bottom:9px;width:12px;height:12px;border-radius:50%;background:var(--mint)}
.brand{display:flex;align-items:center;gap:6px;font-family:"Montserrat",Arial,sans-serif;font-weight:700;color:var(--mint)}
.brand-dot{width:10px;height:10px;border-radius:50%;background:var(--mint)}
/* cover */
.cover-badge{position:absolute;left:50%;top:50%;width:130px;height:130px;margin:-65px 0 0 -65px;border-radius:50%;background:var(--white);display:flex;align-items:center;justify-content:center;box-shadow:0 0 0 5px var(--mint-light)}
.cover-badge .brand{font-size:15px}
.contact-band{position:absolute;left:0;right:0;bottom:0;height:92px;background:rgba(134,207,198,.92);color:var(--white);padding:12px 16px;display:grid;grid-template-columns:1fr 1fr;gap:8px}
.contact-band h4{font-family:"Montserrat",Arial,sans-serif;font-weight:600;font-size:9px;margin-bottom:4px}
.contact-band p{font-size:6.5px;line-height:1.6}
.contact-band .brand{color:var(--white);font-size:9px;grid-column:1 / span 2}
.contact-band .brand-dot{background:var(--white)}
/* product rows */
.item-row{display:flex;gap:10px;align-items:center;margin-top:12px}
.item-row .photo{width:78px;height:78px;flex:none}
.cols{display:flex;gap:9px;margin-top:4px}
.col{flex:1}
.col .photo{width:70px;height:70px;margin:0 auto 8px}
.col .h-title{font-size:8px;text-align:center}
.col .body-text{text-align:center;font-size:5.6px}
.grid6{display:grid;grid-template-columns:1fr 1fr;gap:10px 8px}
.grid6 .cell{display:flex;gap:6px;align-items:center}
.grid6 .photo{width:40px;height:40px;flex:none;border-width:2px}
.grid6 .h-title{font-size:6.5px}
.grid6 .body-text{font-size:5px;margin-top:2px}
.trio{display:flex;gap:8px;margin-top:12px}
.trio .photo{width:66px;height:66px}
/* table */
.price-table{width:100%;border-collapse:collapse;margin-top:10px;font-size:5.8px}
.price-table th{background:var(--mint);color:var(--white);font-family:"Montserrat",Arial,sans-serif;font-weight:600;text-align:left;padding:3px 4px;letter-spacing:.5px;font-size:6px}
.price-table td{padding:3px 4px;border-bottom:1px solid var(--white);color:var(--ink-soft)}
.price-table tr:nth-child(even) td{background:rgba(255,255,255,.35)}
.price-table td.num{text-align:right;white-space:nowrap}
</style>
</head>
<body>
<main class="board">

  <!-- Cover spread -->
  <section class="spread">
    <div class="page page--bleed">
      <span class="photo photo--warm" role="img" aria-label="Overhead photo of assorted frosted cupcakes with sprinkles" style="width:100%;height:100%"></span>
      <div class="contact-band">
        <div>
          <h4>Contact Us</h4>
          <p>Phone: 0123 456 789<br>Email: hello@bramblecakes.example</p>
        </div>
        <div>
          <h4>Follow Us</h4>
          <p>www.bramblecakes.example<br>social.example/bramblecakes</p>
        </div>
      </div>
    </div>
    <div class="page page--bleed">
      <span class="photo photo--mint" role="img" aria-label="Close photo of chocolate cupcakes with mint frosting" style="width:100%;height:100%"></span>
      <div class="cover-badge"><div class="brand"><span class="brand-dot"></span>Bramblecakes</div></div>
    </div>
  </section>

  <!-- About spread -->
  <section class="spread">
    <div class="page">
      <h2 class="h-big">ABOUT <span>US</span></h2>
      <p class="body-text">We bake every cupcake by hand in small batches, using plant based ingredients, local flour and fruit, and packaging made from recycled paper. Our recipes are nut free and light on sugar.</p>
      <p class="script">Honest baking, kind to people and planet. Fresh every morning.</p>
      <p class="body-text">Partners receive fresh deliveries three times a week, with display cards and storage advice for each flavour.</p>
      <div class="trio">
        <span class="photo photo--round photo--kitchen" role="img" aria-label="Baker working in the kitchen"></span>
        <span class="photo photo--round photo--carrot" role="img" aria-label="Tray of cupcakes in a box"></span>
        <span class="photo photo--round photo--choc" role="img" aria-label="Chocolate cupcakes on a tray"></span>
      </div>
      <div class="footer">VEGAN CUPCAKES – BRAMBLECAKES</div>
    </div>
    <div class="page">
      <h2 class="h-title" style="font-size:11px">Homemade <span>nut-free blueberry bramblecakes with blueberry vegan meringue frosting</span></h2>
      <p class="body-text">A soft vanilla sponge filled with whole blueberries, topped with a light aquafaba meringue coloured only with fruit.</p>
      <p class="script">Bright, fruity and gently sweet.</p>
      <span class="photo photo--round photo--berry" role="img" aria-label="Blueberry cupcakes with pink frosting and flowers" style="width:150px;height:150px;margin:14px auto 0"></span>
      <div class="mark"></div>
    </div>
  </section>

  <!-- Two products + three columns -->
  <section class="spread">
    <div class="page">
      <h2 class="h-title">Homemade nut-free blueberry bramblecake <span>with blueberry vegan meringue frosting</span></h2>
      <div class="item-row">
        <span class="photo photo--round photo--berry" role="img" aria-label="Blueberry cupcake with pink meringue"></span>
        <p class="body-text">Baked with fresh berries and oat milk. Keeps two days chilled. Sold in boxes of six or twelve.</p>
      </div>
      <h2 class="h-title" style="margin-top:12px">Choco-beetroot bramblecake <span>chocolate icing</span></h2>
      <div class="item-row">
        <span class="photo photo--round photo--choc" role="img" aria-label="Chocolate beetroot cupcake"></span>
        <p class="body-text">Rich cocoa sponge with grated beetroot and a glossy dark chocolate icing. A customer favourite.</p>
      </div>
      <div class="footer">VEGAN CUPCAKES – BRAMBLECAKES</div>
    </div>
    <div class="page">
      <div class="cols">
        <div class="col">
          <span class="photo photo--round photo--choc" role="img" aria-label="Chocolate beetroot cupcake"></span>
          <h3 class="h-title">Choco-beetroot bramblecake <span>with avocado chocolate icing</span></h3>
          <p class="body-text">Moist cocoa sponge, <b>creamy avocado icing</b>, no refined sugar.</p>
        </div>
        <div class="col">
          <span class="photo photo--round photo--berry" role="img" aria-label="Blueberry cupcake with pink frosting"></span>
          <h3 class="h-title">Homemade nut-free blueberry <span>vegan meringue frosting</span></h3>
          <p class="body-text">Fresh berries, <b>light meringue</b>, fruit colour only.</p>
        </div>
        <div class="col">
          <span class="photo photo--round photo--carrot" role="img" aria-label="Carrot cupcake with cream cheese frosting"></span>
          <h3 class="h-title">Carrot bramblecakes <span>with cream cheese frosting</span></h3>
          <p class="body-text">Spiced carrot sponge, <b>cashew free cream</b> topping.</p>
        </div>
      </div>
      <div class="mark"></div>
    </div>
  </section>

  <!-- Three columns + grid -->
  <section class="spread">
    <div class="page">
      <div class="cols">
        <div class="col">
          <span class="photo photo--round photo--choc" role="img" aria-label="Chocolate beetroot cupcake"></span>
          <h3 class="h-title">Choco-beetroot bramblecake <span>with avocado chocolate icing</span></h3>
          <p class="body-text">Deep cocoa flavour with <b>beetroot</b> for a soft crumb.</p>
        </div>
        <div class="col">
          <span class="photo photo--round photo--berry" role="img" aria-label="Blueberry cupcake"></span>
          <h3 class="h-title">Homemade nut-free blueberry bramblecake <span>with blueberry vegan meringue frosting</span></h3>
          <p class="body-text">Light, fruity and <b>nut free</b>.</p>
        </div>
        <div class="col">
          <span class="photo photo--round photo--carrot" role="img" aria-label="Carrot cupcake"></span>
          <h3 class="h-title">Carrot bramblecakes <span>with cream cheese frosting</span></h3>
          <p class="body-text">Warm spices and <b>fresh carrot</b>.</p>
        </div>
      </div>
      <div class="footer">VEGAN CUPCAKES – BRAMBLECAKES</div>
    </div>
    <div class="page">
      <div class="grid6">
        <div class="cell"><span class="photo photo--round photo--choc" role="img" aria-label="Chocolate cupcake"></span><div><h3 class="h-title">Choco-beetroot bramblecake <span>with avocado chocolate icing</span></h3><p class="body-text">Cocoa sponge, avocado icing.</p></div></div>
        <div class="cell"><span class="photo photo--round photo--berry" role="img" aria-label="Blueberry cupcake"></span><div><h3 class="h-title">Choco-beetroot bramblecake <span>with avocado chocolate icing</span></h3><p class="body-text">Cocoa sponge, avocado icing.</p></div></div>
        <div class="cell"><span class="photo photo--round photo--carrot" role="img" aria-label="Carrot cupcake"></span><div><h3 class="h-title">Choco-beetroot bramblecake <span>with avocado chocolate icing</span></h3><p class="body-text">Cocoa sponge, avocado icing.</p></div></div>
        <div class="cell"><span class="photo photo--round photo--choc" role="img" aria-label="Chocolate cupcake"></span><div><h3 class="h-title">Choco-beetroot bramblecake <span>with avocado chocolate icing</span></h3><p class="body-text">Cocoa sponge, avocado icing.</p></div></div>
        <div class="cell"><span class="photo photo--round photo--berry" role="img" aria-label="Blueberry cupcake"></span><div><h3 class="h-title">Choco-beetroot bramblecake <span>with avocado chocolate icing</span></h3><p class="body-text">Cocoa sponge, avocado icing.</p></div></div>
        <div class="cell"><span class="photo photo--round photo--carrot" role="img" aria-label="Carrot cupcake"></span><div><h3 class="h-title">Choco-beetroot bramblecake <span>with avocado chocolate icing</span></h3><p class="body-text">Cocoa sponge, avocado icing.</p></div></div>
      </div>
      <div class="mark"></div>
    </div>
  </section>

  <!-- Pricing spread -->
  <section class="spread spread--center">
    <div class="page">
      <h2 class="h-title" style="font-size:12px">Order Vegan cupcakes – <span style="color:var(--mint);font-weight:600">Bramblecakes</span><br><span>to sell in your cafe or shop!</span></h2>
      <table class="price-table">
        <thead><tr><th>PRODUCT</th><th>RETAIL</th><th>DISCOUNT</th></tr></thead>
        <tbody>
          <tr><td>Choco-beetroot with avocado icing</td><td class="num">$3.00 each</td><td class="num">$2.40 each</td></tr>
          <tr><td>Nut-free blueberry meringue</td><td class="num">$3.20 each</td><td class="num">$2.50 each</td></tr>
          <tr><td>Carrot with cream cheese frosting</td><td class="num">$3.00 each</td><td class="num">$2.40 each</td></tr>
          <tr><td>Choco-beetroot with avocado icing</td><td class="num">$3.00 each</td><td class="num">$2.40 each</td></tr>
          <tr><td>Nut-free blueberry meringue</td><td class="num">$3.20 each</td><td class="num">$2.50 each</td></tr>
          <tr><td>Carrot with cream cheese frosting</td><td class="num">$3.00 each</td><td class="num">$2.40 each</td></tr>
          <tr><td>Choco-beetroot with avocado icing</td><td class="num">$3.00 each</td><td class="num">$2.40 each</td></tr>
          <tr><td>Nut-free blueberry meringue</td><td class="num">$3.20 each</td><td class="num">$2.50 each</td></tr>
          <tr><td>Carrot with cream cheese frosting</td><td class="num">$3.00 each</td><td class="num">$2.40 each</td></tr>
          <tr><td>Choco-beetroot with avocado icing</td><td class="num">$3.00 each</td><td class="num">$2.40 each</td></tr>
        </tbody>
      </table>
      <div class="footer">VEGAN CUPCAKES – BRAMBLECAKES</div>
    </div>
    <div class="page">
      <table class="price-table" style="margin-top:0">
        <thead><tr><th>PRODUCT</th><th>RETAIL</th><th>DISCOUNT</th></tr></thead>
        <tbody>
          <tr><td>Choco-beetroot with avocado icing</td><td class="num">$3.00 each</td><td class="num">$2.40 each</td></tr>
          <tr><td>Nut-free blueberry meringue</td><td class="num">$3.20 each</td><td class="num">$2.50 each</td></tr>
          <tr><td>Carrot with cream cheese frosting</td><td class="num">$3.00 each</td><td class="num">$2.40 each</td></tr>
          <tr><td>Choco-beetroot with avocado icing</td><td class="num">$3.00 each</td><td class="num">$2.40 each</td></tr>
          <tr><td>Nut-free blueberry meringue</td><td class="num">$3.20 each</td><td class="num">$2.50 each</td></tr>
          <tr><td>Carrot with cream cheese frosting</td><td class="num">$3.00 each</td><td class="num">$2.40 each</td></tr>
          <tr><td>Choco-beetroot with avocado icing</td><td class="num">$3.00 each</td><td class="num">$2.40 each</td></tr>
          <tr><td>Nut-free blueberry meringue</td><td class="num">$3.20 each</td><td class="num">$2.50 each</td></tr>
          <tr><td>Carrot with cream cheese frosting</td><td class="num">$3.00 each</td><td class="num">$2.40 each</td></tr>
          <tr><td>Choco-beetroot with avocado icing</td><td class="num">$3.00 each</td><td class="num">$2.40 each</td></tr>
          <tr><td>Nut-free blueberry meringue</td><td class="num">$3.20 each</td><td class="num">$2.50 each</td></tr>
          <tr><td>Carrot with cream cheese frosting</td><td class="num">$3.00 each</td><td class="num">$2.40 each</td></tr>
        </tbody>
      </table>
      <div class="mark"></div>
    </div>
  </section>

</main>
</body>
</html>
```